Help keep hoosiers happy and at home!

We need a billboard designed for our Indiana based healthcare business called 'Willow Hearth Caregivers'. We administer a medicaid waiver program that provides support and financial aid to live in caregivers that take care of someone who would otherwise be in a nursing home or skilled nursing facility. Qualified caregivers could be eligible to receive up to 1200 dollars a month in tax free financial aid, as well as access to nursing support that helps manage any unexpected situations or changes in a care recipients condition or care routine. Our program empowers families to keep their loved ones at home and out of the nursing home. NOTE: We believe the tagline at the bottom of our logo is disproportionately small. We would like to see that tagline larger and easier to read. I look forward to seeing your design ideas!

Target Market(s)

Medicaid aged beneficiaries and caregivers.

Industry/Entity Type

Home Healthcare

Colors
0054AA
0677BA
7BADD7
CADEEF
E8F1F8

Requirements
Nice to have
• "Empowering friends and family to care for their loves ones at home. Eligible participants receive up to $15,000 a year, tax free."

```html
<!DOCTYPE html>
<html lang="en">
<head>
<meta charset="UTF-8">
<title>Willow Hearth Caregivers Billboard</title>
<link href="https://fonts.googleapis.com/css2?family=Poppins:wght@400;600;700;800&display=swap" rel="stylesheet">
<style>
  :root {
    --navy: #23307b;
    --cyan: #12a6c6;
    --ink: #111111;
    --panel: #dcdcdc;
    --paper: #f5f5f5;
    --white: #ffffff;
    --stage: #ffffff;
  }
  html, body {
    margin: 0;
    padding: 0;
    width: 960px;
    height: 1200px;
    overflow: hidden;
    background: var(--stage);
    font-family: "Poppins", sans-serif;
  }
  .billboard {
    position: absolute;
    left: 30px;
    top: 412px;
    width: 900px;
    height: 375px;
    overflow: hidden;
    background: linear-gradient(135deg, var(--white) 0%, var(--paper) 60%, #ececec 100%);
    box-shadow: 0 14px 30px rgba(0,0,0,0.18);
  }
  .billboard-shapes {
    position: absolute;
    inset: 0;
  }
  .brand {
    position: absolute;
    left: 36px;
    top: 40px;
    display: flex;
    align-items: center;
    gap: 8px;
  }
  .brand-mark {
    width: 14px;
    height: 14px;
    background: var(--navy);
  }
  .brand-name {
    font-weight: 700;
    font-size: 16px;
    color: var(--navy);
    letter-spacing: 0.2px;
  }
  .headline-top {
    position: absolute;
    left: 39px;
    top: 113px;
    margin: 0;
    font-weight: 700;
    font-size: 38px;
    line-height: 1;
    color: var(--ink);
  }
  .headline-band {
    position: absolute;
    left: 39px;
    top: 155px;
    margin: 0;
    font-weight: 700;
    font-size: 38px;
    line-height: 1;
    color: var(--white);
  }
  .subline {
    position: absolute;
    left: 37px;
    top: 200px;
    margin: 0;
    font-weight: 700;
    font-size: 14.5px;
    color: var(--ink);
  }
  .offer {
    position: absolute;
    left: 36px;
    top: 227px;
    width: 434px;
    height: 65px;
    background: var(--panel);
  }
  .offer-eligible {
    position: absolute;
    left: 12px;
    top: 6px;
    font-size: 15px;
    font-weight: 400;
    color: var(--ink);
  }
  .offer-receive {
    position: absolute;
    left: 12px;
    top: 24px;
    font-size: 28px;
    font-weight: 700;
    line-height: 1.2;
    color: var(--ink);
  }
  .offer-taxfree {
    position: absolute;
    right: 32px;
    top: 5px;
    font-size: 17px;
    font-weight: 700;
    color: var(--navy);
  }
  .offer-amount {
    position: absolute;
    right: 30px;
    top: 18px;
    font-size: 35px;
    font-weight: 700;
    line-height: 1.25;
    color: var(--navy);
  }
  .offer-period {
    position: absolute;
    right: 2px;
    top: 32px;
    transform: translate(50%, -50%) rotate(-90deg);
    transform-origin: center;
    right: 15px;
    font-size: 12px;
    font-weight: 700;
    color: var(--navy);
    white-space: nowrap;
  }
  .contact {
    position: absolute;
    left: 36px;
    top: 318px;
    display: flex;
    align-items: center;
    gap: 10px;
    font-weight: 600;
    font-size: 17px;
    color: var(--white);
  }
  .contact-icon {
    width: 19px;
    height: 19px;
  }
  .contact-divider {
    width: 2px;
    height: 20px;
    background: var(--white);
    margin: 0 4px;
  }
</style>
</head>
<body>
  <section class="billboard">
    <svg class="billboard-shapes" width="900" height="375" viewBox="0 0 900 375">
      <rect class="headline-band-shape" x="0" y="157" width="480" height="37" fill="var(--navy)"/>
      <polygon class="footer-band" points="0,305 566,305 614,375 0,375" fill="var(--navy)"/>
      <polygon class="accent-chevron" points="582,0 600,0 470,176 580,305 566,305 448,176" fill="var(--cyan)"/>
      <defs>
        <linearGradient id="photoTones" x1="0" y1="0" x2="1" y2="1">
          <stop offset="0" stop-color="#efe6d6"/>
          <stop offset="0.45" stop-color="#e6e2dc"/>
          <stop offset="0.75" stop-color="#b9bcb8"/>
          <stop offset="1" stop-color="#d9d9d6"/>
        </linearGradient>
      </defs>
      <polygon class="photo-area" role="img" aria-label="Photo of a young caregiver smiling with an elderly man in glasses, seated together in a bright living room" points="600,0 900,0 900,375 614,375 580,305 470,176" fill="url(#photoTones)"/>
    </svg>

    <div class="brand">
      <span class="brand-mark"></span>
      <span class="brand-name">Willow Hearth Caregivers</span>
    </div>

    <h1 class="headline-top">EMPOWERING</h1>
    <h2 class="headline-band">FRIENDS AND FAMILY</h2>
    <p class="subline">TO CARE FOR THEIR LOVES ONES AT HOME</p>

    <div class="offer">
      <span class="offer-eligible">Eligible participants</span>
      <span class="offer-receive">RECEIVE UP TO</span>
      <span class="offer-taxfree">TAX FREE</span>
      <span class="offer-amount">$15,000</span>
      <span class="offer-period">A YEAR</span>
    </div>

    <div class="contact">
      <svg class="contact-icon" viewBox="0 0 24 24" aria-hidden="true">
        <path fill="#ffffff" d="M6.6 10.8a15.1 15.1 0 0 0 6.6 6.6l2.2-2.2a1 1 0 0 1 1-.25 11.4 11.4 0 0 0 3.6.57 1 1 0 0 1 1 1V20a1 1 0 0 1-1 1A17 17 0 0 1 3 4a1 1 0 0 1 1-1h3.5a1 1 0 0 1 1 1c0 1.25.2 2.45.57 3.57a1 1 0 0 1-.25 1z"/>
      </svg>
      <span class="contact-phone">(800)555-0142</span>
      <span class="contact-divider"></span>
      <svg class="contact-icon" viewBox="0 0 24 24" aria-hidden="true">
        <g fill="none" stroke="#ffffff" stroke-width="1.8">
          <circle cx="12" cy="12" r="9"/>
          <ellipse cx="12" cy="12" rx="4" ry="9"/>
          <line x1="3" y1="12" x2="21" y2="12"/>
          <path d="M5 7h14M5 17h14"/>
        </g>
      </svg>
      <span class="contact-web">www.willowhearthcaregivers.com</span>
    </div>
  </section>
</body>
</html>
```